Snowvale LOGO + Business Card design for a Ski Tour agency

- New start-up international tour agency focused on skiing tours
- Connected with the Alps
- Targeted at Asians
- Business/Brand name: Snowvale

```html
<!DOCTYPE html>
<html lang="en">
<head>
<meta charset="UTF-8">
<title>Snowvale Business Card</title>
<link href="https://fonts.googleapis.com/css2?family=Arimo:wght@400;700&display=swap" rel="stylesheet">
<style>
  :root {
    --page-bg: #1a1a1c;
    --card-bg: #242628;
    --ink-white: #f4f4f4;
    --ink-soft: #d9d9d9;
    --brand-red: #d8232f;
  }
  * { margin: 0; padding: 0; box-sizing: border-box; }
  html, body {
    width: 1200px; height: 800px; overflow: hidden;
    background: var(--page-bg);
    font-family: "Arimo", Arial, sans-serif;
  }
  .canvas {
    position: relative; width: 1200px; height: 800px;
    display: flex; flex-direction: column; align-items: center; justify-content: center; gap: 48px;
  }
  .card {
    position: relative; width: 600px; height: 343px;
    background: var(--card-bg);
    box-shadow: 0 14px 30px rgba(0,0,0,0.55);
  }
  .brand-name { color: var(--ink-white); font-weight: 700; white-space: nowrap; }
  .card-front { display: flex; align-items: center; justify-content: center; }
  .card-front .brand-name { font-size: 58px; }

  .card-back .brand-name {
    position: absolute; left: 48px; top: 50%; transform: translateY(-50%);
    font-size: 40px;
  }
  .divider {
    position: absolute; left: 318px; top: 70px; width: 1.5px; height: 203px;
    background: var(--brand-red);
  }
  .contact { position: absolute; left: 344px; top: 78px; color: var(--ink-soft); }
  .contact-name { font-size: 22px; font-weight: 700; color: var(--ink-white); }
  .contact-role { font-size: 14px; color: var(--brand-red); margin-top: 2px; }
  .contact-address { font-size: 13px; line-height: 17px; margin-top: 14px; }
  .contact-list { list-style: none; margin-top: 10px; }
  .contact-list li { display: flex; align-items: center; gap: 8px; font-size: 13px; line-height: 22px; }
  .contact-list .accent { color: var(--brand-red); }
  .icon { width: 14px; height: 14px; flex: none; }
</style>
</head>
<body>
<main class="canvas">
  <section class="card card-front">
    <span class="brand-name">Snowvale</span>
  </section>

  <section class="card card-back">
    <span class="brand-name">Snowvale</span>
    <div class="divider"></div>
    <div class="contact">
      <p class="contact-name">Liam Carter</p>
      <p class="contact-role">Owner</p>
      <p class="contact-address">PO BOX 456, Ridge Road<br>3rd Lane, Vermont 67890</p>
      <ul class="contact-list">
        <li>
          <svg class="icon" viewBox="0 0 14 14"><circle cx="7" cy="7" r="6.5" fill="none" stroke="#d8232f"/><path d="M4.6 3.8 L5.9 3.6 L6.4 5.2 L5.6 5.8 Q6.4 7.6 8.2 8.4 L8.8 7.6 L10.4 8.1 L10.2 9.4 Q6 9.6 4.6 3.8 Z" fill="#d8232f"/></svg>
          <span>555.210.4477</span>
        </li>
        <li>
          <svg class="icon" viewBox="0 0 14 14"><circle cx="7" cy="7" r="6.5" fill="#d8232f"/><rect x="3.8" y="4.8" width="6.4" height="4.4" fill="none" stroke="#242628" stroke-width="0.9"/><path d="M3.8 4.8 L7 7.4 L10.2 4.8" fill="none" stroke="#242628" stroke-width="0.9"/></svg>
          <span>hello@snowvalemail.com</span>
        </li>
        <li>
          <svg class="icon" viewBox="0 0 14 14"><circle cx="7" cy="7" r="6.5" fill="#d8232f"/><circle cx="7" cy="7" r="3.4" fill="none" stroke="#242628" stroke-width="0.9"/><path d="M3.6 7 H10.4 M7 3.6 V10.4" stroke="#242628" stroke-width="0.8"/></svg>
          <span>www.<span class="accent">snowvaletours</span>.com</span>
        </li>
      </ul>
    </div>
  </section>
</main>
</body>
</html>
```